Business card for Financial Technology company

Hello! We'd like to create business cards for 4 members of our company. Our company is a financial technology business that provides funding for businesses. We want to give it a VC (venture captal) look and feel. Clean, fresh and minimal but with a flair of artistry. I'll include some samples of cards we like. It would be great if the back of the card was artistic (see sample files 1 and 2) and the front of the card was the business info. The name of the company is Brightmoor Capital.

```html
<!DOCTYPE html>
<html lang="en">
<head>
<meta charset="UTF-8">
<title>Brightmoor Capital – Business Cards</title>
<link rel="stylesheet" href="https://fonts.googleapis.com/css2?family=Montserrat:wght@400;800&display=swap">
<style>
  :root {
    --canvas-bg: #e6e6e6;
    --card-white: #ffffff;
    --ink: #0b0b0b;
    --pink: #e91e63;
    --purple: #5b4aa8;
    --navy: #1f1b5c;
    --orange: #f7a823;
    --teal: #2dbba3;
    --shadow: 0 18px 40px rgba(0,0,0,0.18);
  }
  * { margin: 0; padding: 0; box-sizing: border-box; }
  html, body {
    width: 1200px; height: 840px; overflow: hidden;
    background: var(--canvas-bg);
    font-family: "Montserrat", sans-serif;
    color: var(--ink);
  }
  .canvas { position: relative; width: 1200px; height: 840px; }

  .card {
    position: absolute;
    width: 560px; height: 340px;
    box-shadow: var(--shadow);
    overflow: hidden;
  }

  /* Front: contact details */
  .card--front {
    left: 590px; top: 60px;
    background: var(--card-white);
  }
  .brand-mark {
    position: absolute;
    left: 36px; top: 74px;
    width: 170px; height: 170px;
    background: var(--purple);
  }
  .front-info {
    position: absolute;
    left: 236px; top: 40px;
    width: 300px;
  }
  .brand-name {
    font-weight: 800;
    font-size: 30px;
    line-height: 1.05;
    letter-spacing: 0.3px;
    text-transform: uppercase;
    color: var(--ink);
  }
  .person-name {
    margin-top: 14px;
    font-weight: 800;
    font-size: 24px;
    line-height: 1.1;
    letter-spacing: 0.5px;
  }
  .person-title {
    font-weight: 400;
    font-size: 15px;
    margin-top: 2px;
  }
  .contact-list {
    list-style: none;
    margin-top: 12px;
    font-size: 14px;
    font-weight: 400;
  }
  .contact-list li {
    display: flex; align-items: center; gap: 7px;
    margin-bottom: 4px;
    white-space: nowrap;
  }
  .contact-list svg { width: 14px; height: 14px; flex: none; }
  .address {
    margin-top: 8px;
    font-size: 14px;
    line-height: 1.3;
  }

  /* Back: artistic side */
  .card--back { left: 60px; top: 440px; }
  .pattern-field {
    position: absolute; inset: 0;
    background: linear-gradient(135deg,
      var(--pink) 0%, var(--purple) 30%, var(--orange) 55%,
      var(--teal) 75%, var(--navy) 100%);
  }
  .back-frame {
    position: absolute;
    left: 66px; top: 62px; right: 66px; bottom: 62px;
    border: 2px solid var(--card-white);
  }
  .back-panel {
    position: absolute;
    left: 80px; top: 76px; right: 80px; bottom: 76px;
    background: var(--card-white);
    display: flex; align-items: center; justify-content: center; gap: 18px;
  }
  .back-panel .brand-square {
    width: 54px; height: 54px; background: var(--purple); flex: none;
  }
  .back-panel .brand-name { font-size: 36px; }
</style>
</head>
<body>
<main class="canvas">

  <section class="card card--front" aria-label="Business card front">
    <div class="brand-mark" aria-hidden="true"></div>
    <div class="front-info">
      <p class="brand-name">Brightmoor<br>Capital</p>
      <p class="person-name">YOUR NAME</p>
      <p class="person-title">Your Tittle Here</p>
      <ul class="contact-list">
        <li>
          <svg viewBox="0 0 24 24" aria-hidden="true"><path fill="#0b0b0b" d="M6.6 10.8a15.1 15.1 0 0 0 6.6 6.6l2.2-2.2a1 1 0 0 1 1-.25 11.4 11.4 0 0 0 3.6.57 1 1 0 0 1 1 1V20a1 1 0 0 1-1 1A17 17 0 0 1 3 4a1 1 0 0 1 1-1h3.5a1 1 0 0 1 1 1c0 1.25.2 2.45.57 3.6a1 1 0 0 1-.25 1z"/></svg>
          012 345 6789 | Fax 012 345 6789
        </li>
        <li>
          <svg viewBox="0 0 24 24" aria-hidden="true"><path fill="#0b0b0b" d="M2 5h20v14H2z"/><path fill="none" stroke="#fff" stroke-width="1.6" d="M2.5 5.5 12 13l9.5-7.5"/></svg>
          you@brightmoorcap.com
        </li>
        <li>
          <svg viewBox="0 0 24 24" aria-hidden="true"><g fill="none" stroke="#0b0b0b" stroke-width="2"><circle cx="12" cy="12" r="9.5"/><ellipse cx="12" cy="12" rx="4.2" ry="9.5"/><path d="M2.5 12h19"/></g></svg>
          www.Yourwebsite.com
        </li>
      </ul>
      <p class="address">No.000, Your Street, Province,<br>Your Country</p>
    </div>
  </section>

  <section class="card card--back" aria-label="Business card back">
    <div class="pattern-field" role="img" aria-label="Colourful geometric pattern of triangles, half circles and concentric rings"></div>
    <div class="back-frame" aria-hidden="true"></div>
    <div class="back-panel">
      <span class="brand-square" aria-hidden="true"></span>
      <p class="brand-name">Brightmoor<br>Capital</p>
    </div>
  </section>

</main>
</body>
</html>
```